High-End Medical Center Website Design Project

This design is part of a well thought-out project by an experienced project manager / developer. The approved wireframe is attached. Creative interpretations / suggestions based on the layout encouraged.

The design is for a new state-of-the-art medical center located in Dallas, Texas. The target audience would likely be individuals (approx. 60% female /40% male) who are the healthcare decision-makers for their families. They would likely have insurance and be inclined to seek out top-quality care.

Potential clients would choose this client over others in their industry because the medical center is physician owned, meaning it is patient-focused rather than profit-focused. The facility is brand new, featuring the latest technology. (This includes an amazing waiting room featuring WiFi and docking stations.) The physicians are hand-picked by referral only.

The look of the site should be extremely clean. We are going for a well-organized, professional look with a bit of a warm glow (interpret that however you like). Use crisp corners and the colors in the logo.

Think modern, clean with some great use of color / font.

We can get lovely photography of the medical center once construction is complete. Feel free to use an "example image" behind the Featured Area ("Physician Owned. Patient-Focused") if you like. We are open to ideas.

ONE CHANGE REQUESTED IN THE WIREFRAME:

Remove the "Connect" 1/4 page footer area and replace with a quick contact form. You may swap the "Locations" area with the form if desired. Put social media icons at the top left of the page in the top header area.

(Note: Please use social media icons that match the design rather than standard icons. We preferred not placing the icons at the top, but the client requested this. Let's not bring more attention to them than necessary.)
Updates

We're custom programming this site, so there's no need to base it on a template. Also, we would prefer not to use typical "seen everywhere" stock images.Thanks.

Industry/Entity Type

Construction

Requirements
Must have
• Follow the wireframe. This has been approved.
Nice to have
• Examples of what hover states, links or dropdowns might look like.

```html
<!DOCTYPE html>
<html lang="en">
<head>
<meta charset="utf-8">
<title>Nova Medical Center</title>
<link href="https://fonts.googleapis.com/css2?family=Source+Sans+3:ital,wght@0,400;0,600;0,700;0,900;1,400&family=Arimo:ital,wght@0,400;0,700;1,400;1,700&display=swap" rel="stylesheet">
<style>
:root{
  --header:#141414;
  --navy:#1a5ea8;
  --teal:#3aa9bf;
  --teal-light:#4fc3d6;
  --hero-top:#0a8ccd;
  --hero-bottom:#19b8dd;
  --panel:#ececec;
  --footer:#272727;
  --footer-line:#444;
  --field:#4a4a4a;
  --button:#1a8ecf;
  --bar:#0b5cb3;
  --text:#2c2c2c;
}
*{margin:0;padding:0;box-sizing:border-box}
html,body{width:1016px;height:1200px;overflow:hidden;background:#fff}
body{position:relative;font-family:"Arimo",Arial,sans-serif;color:var(--text)}
.abs{position:absolute}
.sans{font-family:"Source Sans 3","Source Sans Pro",sans-serif}

/* header */
.site-header{left:0;top:0;width:1016px;height:100px;background:linear-gradient(#0c0c0c,#262626)}
.social-top{left:86px;top:15px;display:flex;gap:5px}
.social-top a{width:16px;height:16px;background:#2e7fc4;display:block;opacity:.85}
.social-top a:hover{opacity:1}
.call{right:96px;top:14px;color:#ccc;font-size:15px}
.call b{color:var(--teal-light);font-weight:400;margin-left:4px}
.call svg{vertical-align:-3px;margin-left:4px}
.brand{display:flex;align-items:center;gap:8px}
.brand i{display:block;width:22px;height:22px;background:var(--teal)}
.brand span{color:#fff;font-weight:700;font-size:24px;letter-spacing:1px;font-family:"Source Sans 3",sans-serif}
.brand-top{left:86px;top:48px}
.nav{left:380px;top:59px;display:flex}
.nav a{color:#fff;text-decoration:none;font-size:15.5px;padding:0 19px;border-left:1px solid #3a3a3a;line-height:24px}
.nav a:first-child{border-left:none}
.nav a:hover{color:var(--teal-light)}

/* headline */
.headline{left:0;top:100px;width:1016px;height:96px;background:linear-gradient(#e9e9e9,#fff 40%);text-align:center;line-height:96px;font-size:43px;font-weight:900;letter-spacing:1px}
.headline .a{color:var(--navy)}
.headline .b{color:var(--teal);margin-left:18px}

/* hero */
.hero{left:0;top:196px;width:1016px;height:306px;background:linear-gradient(var(--hero-top),var(--hero-bottom))}
.badge{width:190px;height:190px;border-radius:50%;background:#fff;top:54px;display:flex;align-items:center;justify-content:center}
.badge .inner{width:172px;height:172px;border-radius:50%;background:radial-gradient(#f7f7f7,#dcdcdc);display:flex;align-items:center;justify-content:center}
.badge .art{width:100px;height:100px;border-radius:50%}
.shadow{top:262px;width:150px;height:12px;border-radius:50%;background:radial-gradient(rgba(0,40,80,.45),transparent 70%)}

/* features */
.features{left:0;top:502px;width:1016px;height:204px;background:var(--panel);border-top:1px solid #d6d6d6;border-bottom:1px solid #d6d6d6}
.apart{left:91px;top:32px;width:170px;font-weight:700;text-transform:uppercase;font-size:28px;line-height:34px}
.apart .l1{color:var(--teal)}
.apart .l2{color:#333;padding-left:62px}
.apart .l3{color:var(--navy);padding-left:31px;display:flex;align-items:center;gap:2px}
.feature{top:40px;width:182px}
.feature h3{color:var(--navy);font-weight:600;font-size:21px;margin-bottom:10px}
.feature p{font-size:11px;line-height:17px;color:#333;letter-spacing:.4px}
.vline{width:1px;background:#d0d0d0;top:30px;height:156px}

/* content */
.photo{left:91px;top:741px;width:191px;height:196px;border:4px solid #e4e4e4;background:linear-gradient(135deg,#d9c3b3,#f1ece6 55%,#9fc7d3)}
.section-title{color:var(--teal);font-weight:600;font-size:23px;letter-spacing:.4px}
.story{left:300px;top:780px;width:314px;font-size:10.6px;line-height:17px;text-align:justify;color:#333}
.story em{font-weight:700}
.content-divider{left:650px;top:722px;width:1px;height:240px;background:linear-gradient(transparent,#ddd 20%,#ddd 80%,transparent)}
.quote{left:676px;top:782px;width:234px;font-style:italic;font-size:10px;line-height:17px;color:#333}
.quote .mark{font-size:26px;color:#555;font-style:normal;font-family:Georgia,serif;vertical-align:-8px;line-height:0}
.avatar{left:850px;top:842px;width:68px;height:58px;border:3px solid #e8e8e8;background:linear-gradient(#c9a483,#e3c7a7)}
.byline{right:175px;top:869px;text-align:right;font-style:italic;font-size:10.5px;line-height:17px;color:#333}
.byline small{color:var(--navy);font-size:9.5px}

/* footer */
.site-footer{left:0;top:987px;width:1016px;height:187px;background:var(--footer)}
.fcol h4{color:var(--teal);font-weight:600;font-size:17px;margin-bottom:9px;font-family:"Source Sans 3",sans-serif}
.fcol ul{list-style:none}
.fcol li{font-size:10.6px;line-height:22px}
.fcol a{color:#eee;text-decoration:none}
.fcol a:hover{color:var(--teal-light)}
.fdiv{width:1px;background:var(--footer-line);top:35px;height:130px}
.quick-contact{display:flex;flex-direction:column;gap:5px;width:150px}
.quick-contact input,.quick-contact textarea{background:var(--field);border:none;color:#ddd;font:10.5px "Arimo",sans-serif;padding:0 7px;height:21px;outline:none}
.quick-contact textarea{height:34px;padding-top:5px;resize:none}
.quick-contact input::placeholder,.quick-contact textarea::placeholder{color:#bbb}
.quick-contact button{align-self:flex-end;background:var(--button);border:none;color:#fff;font:700 10.5px "Arimo",sans-serif;height:21px;width:64px;cursor:pointer}
.quick-contact button:hover{background:var(--teal-light)}
.brand-foot{left:725px;top:1047px}
.brand-foot span{font-size:25px}
.address{right:105px;top:1098px;text-align:right;color:#eee;font-size:10.6px;line-height:15px}
.bottom-bar{left:0;top:1174px;width:1016px;height:26px;background:var(--bar);color:#fff;text-align:center;font-size:11px;line-height:26px}
.bottom-bar a{color:#fff;text-decoration:none}
</style>
</head>
<body>

<header class="site-header abs">
  <div class="social-top abs" aria-label="Social links"><a href="#" aria-label="Social link 1"></a><a href="#" aria-label="Social link 2"></a><a href="#" aria-label="Social link 3"></a></div>
  <div class="call abs sans">Call Now
    <svg width="22" height="16" viewBox="0 0 22 16" aria-hidden="true"><path d="M2 6c0-3 4-5 9-5s9 2 9 5l-1 2h-4l-1-3h-6L7 8H3z M5 9h12l2 6H3z" fill="#2a8fd0"/><circle cx="11" cy="12" r="2" fill="#141414"/></svg>
    <b>(555) 014-2290</b></div>
  <div class="brand brand-top abs"><i></i><span>NOVA MEDICAL CENTER</span></div>
  <nav class="nav abs sans">
    <a href="#">Why Nova</a><a href="#">Physicians</a><a href="#">Specialties</a><a href="#">Info</a><a href="#">Location</a><a href="#">Contact</a>
  </nav>
</header>

<section class="headline abs sans"><span class="a">PHYSICIAN OWNED</span><span class="b">PATIENT FOWSED</span></section>

<section class="hero abs">
  <div class="badge abs" style="left:115px"><div class="inner"><div class="art" role="img" aria-label="Stethoscope illustration" style="background:radial-gradient(#7fa8e0,#2b5fbf)"></div></div></div>
  <div class="badge abs" style="left:401px"><div class="inner"><div class="art" role="img" aria-label="Blue book illustration" style="background:radial-gradient(#6f93e6,#2c4fb8)"></div></div></div>
  <div class="badge abs" style="left:688px"><div class="inner"><div class="art" role="img" aria-label="Question mark help illustration" style="background:radial-gradient(#4f86ea,#1c48c4)"></div></div></div>
  <div class="shadow abs" style="left:135px"></div>
  <div class="shadow abs" style="left:421px"></div>
  <div class="shadow abs" style="left:708px"></div>
</section>

<section class="features abs">
  <div class="apart abs sans">
    <div class="l1">What set</div>
    <div class="l2">us</div>
    <div class="l3">Aport
      <svg width="44" height="40" viewBox="0 0 44 40" aria-hidden="true"><path d="M0 0h12l16 20-16 20H0l16-20z" fill="#8a8a8a"/><path d="M14 0h12l16 20-16 20H14l16-20z" fill="#333"/></svg>
    </div>
  </div>
  <div class="vline abs" style="left:284px"></div>
  <div class="vline abs" style="left:510px"></div>
  <div class="vline abs" style="left:730px"></div>
  <div class="feature abs" style="left:306px"><h3 class="sans">Technology</h3><p>simply dummy text of the printing and typesetting industry. Lorem Ipsum has been the industry's standard dummy text ever since the 1500s,</p></div>
  <div class="feature abs" style="left:528px"><h3 class="sans">Quality of Care</h3><p>simply dummy text of the printing and typesetting industry. Lorem Ipsum has been the industry's standard dummy text ever since the 1500s,</p></div>
  <div class="feature abs" style="left:747px"><h3 class="sans">Patient Experience</h3><p>simply dummy text of the printing and typesetting industry. Lorem Ipsum has been the industry's standard dummy text ever since the 1500s,</p></div>
</section>

<div class="photo abs" role="img" aria-label="Photo of a therapist giving a patient a facial treatment"></div>
<h2 class="section-title sans abs" style="left:300px;top:739px">90 Seconds to Better Health</h2>
<div class="story abs">
  <p><em><i>Lorem Ipsum is simply dummy text of the printing and typesetting industry. Lorem Ipsum has</i></em> been the industry's standard dummy text ever since the 1500s, when an unknown printer took a galley of type and scrambled it to make a type specimen book.</p>
  <p style="margin-top:17px">It has survived not only five centuries, but also the leap into electronic typesetting, remaining essentially unchanged. It was popularised in the 1960s with the release of Letraset sheets containing Lorem Ipsum passages,</p>
</div>
<div class="content-divider abs"></div>
<h2 class="section-title sans abs" style="left:676px;top:739px">Testimonials</h2>
<div class="quote abs sans"><span class="mark">&ldquo;</span> Suspendisse lobortis turpis in odio blandit ac interdum lorem euismod. Aenean a nibh eget turpis vehicula tempus ac sed massa..... <span class="mark">&rdquo;</span></div>
<div class="byline abs sans">By Daniel Reyes<br><small>Posted on Nov25, 2012</small></div>
<div class="avatar abs" role="img" aria-label="Portrait photo of the reviewer"></div>

<footer class="site-footer abs">
  <div class="fcol abs" style="left:114px;top:14px"><h4>News</h4><ul><li><a href="#">About Us</a></li><li><a href="#">Raw Education</a></li><li><a href="#">Resources</a></li><li><a href="#">Blog</a></li><li><a href="#">Newsletter</a></li><li><a href="#">Contact Us</a></li></ul></div>
  <div class="fdiv abs" style="left:237px"></div>
  <div class="fcol abs" style="left:259px;top:14px"><h4>Blog</h4><ul><li><a href="#">Specials</a></li><li><a href="#">Pre-Mixed Meals</a></li><li><a href="#">Fish</a></li><li><a href="#">Meat Blends</a></li><li><a href="#">Organ Meats</a></li><li><a href="#">Raw Meaty Bones</a></li></ul></div>
  <div class="fdiv abs" style="left:378px"></div>
  <div class="fcol abs" style="left:396px;top:14px">
    <h4>Quick Contact</h4>
    <form class="quick-contact" action="#">
      <input type="text" placeholder="Your name">
      <input type="email" placeholder="Email address">
      <textarea placeholder="Message"></textarea>
      <button type="submit">SEND</button>
    </form>
  </div>
  <div class="fdiv abs" style="left:561px"></div>
  <div class="fcol abs" style="left:577px;top:14px"><h4>Locations</h4><ul><li><a href="#">Shipping &amp; Returns</a></li><li><a href="#">Gift Certificates</a></li><li><a href="#">Privacy Policy</a></li><li><a href="#">Terms and Conditions</a></li><li><a href="#">FAQ's</a></li><li><a href="#">Sitemap</a></li></ul></div>
  <div class="fdiv abs" style="left:711px"></div>
  <div class="fcol abs" style="left:724px;top:14px"><h4>Average Wait Time</h4></div>
</footer>
<div class="brand brand-foot abs"><i></i><span>NOVA MEDICAL</span></div>
<div class="address abs">#208-4470 Harbourview Lane<br>Fairhaven, BC, V2R 8K4<br>Fax: 555-014-2291</div>
<div class="bottom-bar abs">Copyright &copy; 2013 All rights reserved | <a href="#">Privacy Policy</a></div>

</body>
</html>
```